Corporate Website - KWARTA HOLDINGS, LLC

This Nevada Corporation has several subsidiaries:
T. M. Designs - Interior Design; Commercial, Residential & Hospitality
T. M. Style - Fashion Design & Styling
FERN LOUNGE - Upscale Membership Only Lounge servicing Business Men and women. It is located in Accra, Ghana
FERN SUITES - Full Service Executive Suites for top Businesses. Located in Accra, Ghana.
THE MATERIAL YARD - Distributor for Building and Interior Design Materials
URL: www.kwartaholdingsllc.example
Website: info@kwartaholdingsllc.example
Phones: 1 702-555-0147 Las Vegas; +233 26 5550193 Ghana

Industry/Entity Type

Fashion

```html
<!DOCTYPE html>
<html lang="en">
<head>
<meta charset="utf-8">
<title>Kwarta Holdings, LLC</title>
<link rel="stylesheet" href="https://fonts.googleapis.com/css2?family=Advent+Pro:wght@300;400;600&family=Yanone+Kaffeesatz:wght@300;400;500;600&family=Lato:wght@300;400&display=swap">
<style>
:root{
  --topbar:#0c0607;
  --header:#0a0a0a;
  --accent:#2fa8d0;
  --ink:#111;
  --muted:#555b60;
  --footer:#2c3438;
  --footer-deep:#1f2528;
  --white:#fff;
  --steel:#4d7ea6;
}
*{margin:0;padding:0;box-sizing:border-box}
html,body{width:1047px;height:1200px;overflow:hidden;background:var(--white)}
body{position:relative;font-family:"Yanone Kaffeesatz",sans-serif;color:var(--ink)}
.abs{position:absolute}

.topbar{left:0;top:0;width:1047px;height:27px;background:var(--topbar);color:var(--white);font-size:11px;font-weight:500}
.topbar .contacts{left:78px;top:6px;display:flex;gap:6px;align-items:center}
.topbar .contacts svg{width:9px;height:9px;fill:var(--white);margin-right:3px;vertical-align:-1px}
.social-top{right:84px;top:9px;display:flex;gap:20px}
.social-top span{width:8px;height:8px;background:var(--white);display:block}

.site-header{left:0;top:27px;width:1047px;height:93px;background:var(--header)}
.brand{left:76px;top:61px;color:var(--white);font-size:22px;font-weight:500;letter-spacing:.3px;z-index:2}
.nav{right:86px;top:68px;display:flex;gap:16px;font-size:11px;color:var(--accent);font-weight:500;z-index:2}
.nav .contact{margin-left:27px;display:flex;gap:5px;align-items:center}
.nav svg{width:11px;height:9px;stroke:var(--accent);fill:none}

.hero{left:0;top:120px;width:1047px;height:346px;
  background:linear-gradient(180deg,#d8dcd8 0%,#b5ad9e 30%,#6f4a2c 60%,#5a351c 100%)}
.hero::after{content:"";position:absolute;inset:0;background:radial-gradient(ellipse at 38% 30%,rgba(50,110,50,.55),transparent 30%)}
.hero-card{left:75px;top:248px;width:280px;height:167px;background:rgba(255,255,255,.72);padding:24px 0 0 23px;font-family:"Advent Pro",sans-serif;font-weight:300;font-size:28px;line-height:30px;color:var(--ink);z-index:2}
.hero-card strong{font-family:"Yanone Kaffeesatz",sans-serif;font-weight:500;font-size:30px;letter-spacing:.5px}

.callout{left:0;top:466px;width:1047px;height:154px;background:var(--white)}
.callout h2{left:78px;top:54px;width:650px;font-family:"Advent Pro",sans-serif;font-weight:300;font-size:28px;line-height:31px;color:var(--muted)}
.callout h2 b{font-weight:600;color:#333}
.btn-dark{left:759px;top:59px;width:178px;height:40px;background:var(--ink);color:var(--white);font-size:22px;display:flex;align-items:center;padding-left:12px;gap:12px}
.btn svg{fill:none;stroke:currentColor;stroke-width:2}

.suites{left:0;top:620px;width:1047px;height:301px;
  background:linear-gradient(90deg,#cfcbc6 0%,#6b4b3c 35%,#4b3328 60%,#8a7d74 100%)}
.suites-band{left:0;top:670px;width:1047px;height:220px;background:rgba(255,255,255,.86)}
.suites-icon{left:178px;top:721px}
.suites-name{left:171px;top:814px;font-size:24px;color:var(--ink);font-weight:400}
.suites-text{left:380px;top:737px;width:600px;font-family:"Lato",sans-serif;font-weight:300;font-size:22px;line-height:26px;color:#222}
.btn-steel{left:828px;top:807px;width:134px;height:41px;background:var(--steel);border:1px solid #dfe6ec;color:var(--white);font-size:13px;display:flex;align-items:center;padding-left:12px;gap:10px}

.footer{left:0;top:921px;width:1047px;height:221px;background:var(--footer)}
.footer-brand{left:78px;top:940px;font-size:24px;font-weight:500;color:var(--white)}
.footer-about{left:78px;top:982px;width:420px;font-size:10.6px;line-height:15px;font-weight:600;color:var(--white)}
.footer-mail{left:78px;top:1056px;width:419px;height:31px;border:1px solid #d6d9db;display:flex;align-items:center;justify-content:center;gap:6px;font-family:"Lato",sans-serif;font-size:11px;color:var(--white)}
.footer-mail svg{width:10px;height:10px;fill:none;stroke:var(--white)}
.footer-phones{left:80px;top:1094px;font-size:15px;line-height:16px;font-weight:500;color:var(--white)}
.footer-phones svg{width:11px;height:11px;fill:var(--white);vertical-align:-1px;margin-right:3px}
.touch{left:760px;top:965px;width:190px;border-bottom:1px solid #e0e0e0;font-family:"Advent Pro",sans-serif;font-size:16px;padding-bottom:3px;color:var(--white)}
.touch-icons{left:758px;top:1000px;width:112px;height:28px;background:#0c0c0c;display:flex;justify-content:space-around;align-items:center;border-top:2px solid var(--accent)}
.touch-icons span{width:8px;height:8px;background:var(--white);display:block}
.to-top{left:964px;top:1107px;width:40px;height:36px;background:#333b3f;border:1px solid #3b4448;display:flex;align-items:center;justify-content:center}

.bottom{left:0;top:1142px;width:1047px;height:58px;background:var(--footer-deep)}
.copyright{left:78px;top:1169px;font-family:"Lato",sans-serif;font-size:8px;color:#e6e6e6}
.up-arrow{left:953px;top:1168px}
</style>
</head>
<body>

<div class="abs topbar">
  <div class="abs contacts">
    <span><svg viewBox="0 0 10 10"><path d="M2 0l2 2-1 1.5c.8 1.6 2 2.7 3.5 3.5L8 6l2 2-1.5 2C4 9.5.5 6 0 1.5z"/></svg>+1 (702) 555-0147 ( LAS VEGAS )</span><span>|</span>
    <span><svg viewBox="0 0 10 10"><path d="M2 0l2 2-1 1.5c.8 1.6 2 2.7 3.5 3.5L8 6l2 2-1.5 2C4 9.5.5 6 0 1.5z"/></svg>+233 26 5550193 ( GHANA )</span><span>|</span>
    <span><svg viewBox="0 0 10 10"><path d="M0 1h10v8H0z M0 1l5 4 5-4" fill="none" stroke="#fff"/></svg>info@kwartaholdingsllc.example</span>
  </div>
  <div class="abs social-top"><span></span><span></span><span></span><span></span></div>
</div>

<header class="abs site-header"></header>
<div class="abs brand">KWARTA HOLDINGS, LLC</div>
<nav class="abs nav">
  <span>SERVICES</span><span>ABOUT US</span><span>PAGE 1</span>
  <span class="contact"><svg viewBox="0 0 11 9"><path d="M.5.5h10v8H.5z M.5.5l5 4 5-4"/></svg>CONTACT</span>
</nav>

<div class="abs hero" role="img" aria-label="Photo of a bright open-plan loft interior with wooden floor, indoor planter and long dining table"></div>
<div class="abs hero-card"><strong>THE MATERIAL YARD</strong> –<br>Distributor for<br>Building and Interior<br>Design Materials</div>

<section class="abs callout">
  <h2 class="abs">Your <b>Trusted</b> Resource for Commercial Building and Interior Design Materials</h2>
  <div class="abs btn btn-dark">Send an enquiry
    <svg width="26" height="26" viewBox="0 0 26 26"><circle cx="13" cy="13" r="11.5"/><path d="M7 13h11M14 9l4 4-4 4"/></svg>
  </div>
</section>

<div class="abs suites" role="img" aria-label="Photo of an executive office atrium with wood-panelled walls and two businesswomen talking"></div>
<div class="abs suites-band"></div>
<svg class="abs suites-icon" width="78" height="78" viewBox="0 0 78 78">
  <circle cx="39" cy="39" r="35" fill="none" stroke="#2fa8d0" stroke-width="5"/>
  <circle cx="37" cy="32" r="10" fill="#2fa8d0"/>
  <path d="M21 58c0-10 7-15 16-15s16 5 16 15z" fill="#2fa8d0"/>
  <path d="M52 24h8M56 20v8" stroke="#2fa8d0" stroke-width="2.5"/>
</svg>
<div class="abs suites-name">FERN SUITES</div>
<p class="abs suites-text">Full Service Executive Suites for top Businesses. Located in Accra, Ghana.</p>
<div class="abs btn btn-steel">Send an enquiry
  <svg width="26" height="26" viewBox="0 0 26 26"><circle cx="13" cy="13" r="11.5"/><path d="M7 13h11M14 9l4 4-4 4"/></svg>
</div>

<footer class="abs footer"></footer>
<div class="abs footer-brand">KWARTA HOLDINGS, LLC</div>
<p class="abs footer-about">Lorem ipsum is demo text is to preview. Here goes some information about company,. a short description. Lorem ipsum is demo text is to preview. Here goes some information about company,. a short description. Lorem ipsum is demo text is to preview. Here goes some information about company,. a short description. Lorem ipsum is demo text is to preview. Here goes some information about company,. a short description.</p>
<div class="abs footer-mail"><svg viewBox="0 0 10 10"><path d="M9.5.5L.5 4.5l4 1 1 4z M9.5.5l-5 5"/></svg>info@kwartaholdingsllc.example</div>
<div class="abs footer-phones">
  <div><svg viewBox="0 0 10 10"><path d="M2 0l2 2-1 1.5c.8 1.6 2 2.7 3.5 3.5L8 6l2 2-1.5 2C4 9.5.5 6 0 1.5z"/></svg>+1 (702) 555-0147 ( Las Vegas )</div>
  <div><svg viewBox="0 0 10 10"><path d="M2 0l2 2-1 1.5c.8 1.6 2 2.7 3.5 3.5L8 6l2 2-1.5 2C4 9.5.5 6 0 1.5z"/></svg>+233 26 5550193 ( Ghana )</div>
</div>
<div class="abs touch">Stay in touch</div>
<div class="abs touch-icons"><span></span><span></span><span></span><span></span></div>
<div class="abs to-top"><svg width="10" height="6" viewBox="0 0 10 6"><path d="M1 5l4-4 4 4" fill="none" stroke="#9aa3a7" stroke-width="1.2"/></svg></div>

<div class="abs bottom"></div>
<div class="abs copyright">© 2015 Kwarta Holdings, LLC | All Rights Reserved | Developed by Ravi ( mail@ravi.example )</div>
<svg class="abs up-arrow" width="10" height="10" viewBox="0 0 10 10"><path d="M5 9V2M1.5 5L5 1.5 8.5 5" fill="none" stroke="#fff" stroke-width="2"/></svg>

</body>
</html>
```